Micro Loan Promo Business Card

HI Designers,

I am in the process of getting funding for a new Gluten free Pancake food cart in San Francisco and part of the way i am looking to fund it is through micro loans.

I have a current brand and business card already and need a fun exciting card that I can hand out to people that are interested in getting involved for as little as $10 or as much as $5000.

This card will tie in with a page on the website, tobalux.com that is currently being built the home page of which will feature a black and white image of a food truck that gets colored in as the funding goal is reached one part at a time, a wheel a window etc.(I'll post that project on Pixel Forum as well). I'd like the card to focus on this showing an active movement with the truck filling with color like a thermometer.

Im open to see what text and ideas you have on how to best convey this with keeping with the "Must Haves' and will join the discussion once we are underway. I want a grass roots personal feel targeted for 30-40 year olds hip and fun.

Welcome to the team and I look forward to collaborating with you.

Tam Oliphe
Owner/ Chef
Tobin's On the Burn
Updates

Industry/Entity Type

Requirements
Must have
• Needs to have a picture of a Food Truck with excited people inside

The logo for 'Tobin's On the Burn'

The text "Let your Money Make you Money" and " Be a part of building something great!"

Web address :
TobaLux.com

```html
<!DOCTYPE html>
<html lang="en">
<head>
<meta charset="utf-8">
<title>Tobin's On the Burn – Micro Loan Cards</title>
<link rel="stylesheet" href="https://fonts.googleapis.com/css2?family=Oswald:wght@500;600&family=Kalam:wght@400&display=swap">
<style>
  :root {
    --backdrop: #4a4a4a;
    --sky: #18a0d6;
    --sky-light: #4cbbe4;
    --hill-dark: #3b9a3c;
    --hill-light: #8cc63f;
    --soil: #a4490f;
    --soil-text: #f4ec7a;
    --white: #ffffff;
    --brand-blue: #1595cf;
    --truck-green: #7dbb3a;
    --crowd: #1c1c1c;
  }
  * { box-sizing: border-box; margin: 0; padding: 0; }
  html, body { width: 1200px; height: 600px; overflow: hidden; }
  body {
    background: var(--backdrop);
    position: relative;
    font-family: "Oswald", "Arial Narrow", sans-serif;
  }

  .card {
    position: absolute;
    overflow: hidden;
    box-shadow: 0 4px 14px rgba(0,0,0,0.35);
  }

  /* ---------- Front card (landscape) ---------- */
  .card--front {
    left: 220px; top: 168px;
    width: 464px; height: 264px;
    background: linear-gradient(180deg, var(--sky) 0%, var(--sky-light) 100%);
  }
  .card__quote {
    font-family: "Kalam", "Comic Sans MS", cursive;
    color: var(--white);
    font-size: 13px;
    letter-spacing: 0.5px;
    white-space: nowrap;
  }
  .card--front .card__quote { position: absolute; left: 20px; top: 6px; }

  .brand {
    position: absolute;
    color: var(--white);
    font-weight: 600;
    text-transform: uppercase;
    line-height: 0.95;
    text-align: center;
  }
  .brand__line--main { display: block; font-size: 46px; letter-spacing: 1px; }
  .brand__line--sub { display: block; font-size: 29px; letter-spacing: 1px; }
  .card--front .brand { left: 18px; top: 40px; width: 190px; }

  .tagline {
    position: absolute;
    color: var(--white);
    font-size: 11px;
    font-weight: 500;
    letter-spacing: 3px;
    text-transform: uppercase;
    white-space: nowrap;
  }
  .card--front .tagline { left: 0; width: 226px; text-align: center; top: 118px; }

  .scenery {
    position: absolute;
    background: linear-gradient(180deg, var(--hill-dark) 0%, var(--hill-light) 55%, var(--hill-light) 100%);
  }
  .card--front .scenery { left: 0; bottom: 18px; width: 464px; height: 110px; }

  .truck-crowd {
    position: absolute;
    left: 212px; top: 42px;
    width: 240px; height: 186px;
    background: linear-gradient(180deg, var(--truck-green) 0%, var(--truck-green) 45%, var(--crowd) 100%);
    border-radius: 6px;
  }

  .soil-band {
    position: absolute; left: 0; bottom: 0;
    width: 100%;
    background: var(--soil);
    color: var(--soil-text);
    font-weight: 500;
    text-transform: uppercase;
    text-align: center;
    white-space: nowrap;
  }
  .card--front .soil-band {
    height: 18px; font-size: 9.5px; line-height: 18px; letter-spacing: 0.6px;
  }

  /* ---------- Back card (portrait) ---------- */
  .card--back {
    left: 714px; top: 68px;
    width: 264px; height: 462px;
    background: linear-gradient(180deg, var(--sky) 0%, var(--sky) 48%, var(--white) 66%, var(--white) 100%);
  }
  .card--back .card__quote {
    position: absolute; left: 0; top: 22px; width: 100%;
    text-align: center; font-size: 12.5px;
  }
  .card--back .brand { left: 0; top: 70px; width: 100%; }
  .card--back .brand__line--main { font-size: 54px; }
  .card--back .brand__line--sub { font-size: 34px; }
  .card--back .tagline { left: 0; top: 170px; width: 100%; text-align: center; }

  .card--back .scenery { left: 30px; top: 240px; width: 208px; height: 73px; }
  .card--back .soil-band {
    left: 30px; bottom: auto; top: 313px;
    width: 208px; height: 17px;
    font-size: 10px; line-height: 17px; letter-spacing: 3px;
  }

  .visit {
    position: absolute; left: 0; width: 100%;
    text-align: center;
    color: var(--brand-blue);
    font-weight: 500;
    text-transform: uppercase;
    white-space: nowrap;
  }
  .visit--lead { top: 362px; font-size: 17px; letter-spacing: 0.5px; }
  .visit--url { top: 390px; font-size: 25px; font-weight: 600; letter-spacing: 0.5px; }
</style>
</head>
<body>

  <section class="card card--front" aria-label="Front of card">
    <p class="card__quote">“Be a part of building something great”</p>

    <div class="brand">
      <span class="brand__line--main">Tobin's</span>
      <span class="brand__line--sub">On the Burn</span>
    </div>

    <div class="scenery" role="img" aria-label="Illustration of rolling green hills with a yellow picket fence"></div>

    <p class="tagline">• Freshly Milled •</p>

    <div class="truck-crowd" role="img" aria-label="Illustration of a green food truck with a waving chef inside and a cheering crowd in silhouette"></div>

    <p class="soil-band">• Gluten free street style pancakes and baking mixes •</p>
  </section>

  <section class="card card--back" aria-label="Back of card">
    <p class="card__quote">“Let your Money Make you Money”</p>

    <div class="brand">
      <span class="brand__line--main">Tobin's</span>
      <span class="brand__line--sub">On the Burn</span>
    </div>

    <p class="tagline">• Freshly Milled •</p>

    <div class="scenery" role="img" aria-label="Illustration of rolling green hills with a yellow picket fence"></div>

    <p class="soil-band">• Gluten Free •</p>

    <p class="visit visit--lead">To find out more visit...</p>
    <p class="visit visit--url">www.tobalux.com</p>
  </section>

</body>
</html>
```